8 1/2 x 8 1/2 Social Media Design Ad - Commercial Loan Originator

Wanted
Commercial Loan Originators

* No Licensing Required
* Lend Nationwide with few exceptions
* Competitive Compensation
* You find the Investors and we handle the rest!!!

PRODUCTS
* Debt Service Coverage Loans (DSCR)
* Fix & Flip Financing
* Ground Up Construction
* Bridge Loans
* Portfolio Loans
And many more.....

Call (800) 417-9265 x24 for more information

Brightmoor Lending Partners, Inc.
7200 Warbleton Avenue, Harrow Springs, MD 21987
NMLS #318640

```html
<!DOCTYPE html>
<html lang="en">
<head>
<meta charset="utf-8">
<title>Commercial Loan Originators – Brightmoor Lending Partners</title>
<link href="https://fonts.googleapis.com/css2?family=Bebas+Neue&family=Montserrat:wght@500;700;800&display=swap" rel="stylesheet">
<style>
:root{
  --page:#e6e6e6;
  --ink:#0b0d1a;
  --navy:#1c2a6b;
  --royal:#263f9a;
  --gold:#e6b84f;
  --gold-deep:#d9a53a;
  --cream:#fbeac0;
  --white:#ffffff;
}
*{margin:0;padding:0;box-sizing:border-box}
html,body{width:677px;height:1200px;overflow:hidden;background:var(--page)}
.ad{
  position:absolute;left:18px;top:280px;width:640px;height:640px;
  background:var(--ink);overflow:hidden;
  font-family:"Montserrat",sans-serif;color:var(--white);
}
.hero-photo{
  position:absolute;left:240px;top:0;width:400px;height:322px;
  background:
    linear-gradient(90deg,var(--ink) 0%,rgba(11,13,26,0) 35%),
    radial-gradient(ellipse at 70% 40%,#c9d4e4 0%,#6f86a8 40%,#243552 80%);
}
.brand{position:absolute;left:30px;top:26px;width:220px;text-align:center}
.brand-mark{width:58px;height:58px;border:3px solid var(--gold);border-radius:50%;margin:0 auto 10px}
.brand-name{font-weight:800;font-size:17px;line-height:1.2;color:var(--gold);text-transform:uppercase;letter-spacing:.5px}
.headline{position:absolute;left:29px;top:176px;font-family:"Bebas Neue",sans-serif;line-height:.86}
.headline-main{display:block;font-size:90px;color:var(--gold);letter-spacing:-.5px}
.headline-sub{display:block;font-size:63px;color:var(--white);letter-spacing:-.3px}
.rule{position:absolute;left:0;width:640px;height:6px;background:var(--gold)}
.benefits{
  position:absolute;left:0;top:328px;width:640px;height:80px;
  background:linear-gradient(90deg,var(--gold-deep) 0%,var(--gold) 40%,var(--cream) 70%,var(--cream) 100%);
  display:flex;align-items:center;padding-left:29px;
}
.benefit-col{list-style:none;display:flex;flex-direction:column;gap:8px}
.benefit-col + .benefit-col{margin-left:10px;padding-left:12px;border-left:1.5px solid var(--navy)}
.benefit{display:flex;align-items:flex-start;gap:8px;font-weight:800;font-size:15.5px;line-height:.98;color:var(--navy);text-transform:uppercase;letter-spacing:.2px}
.tick{flex:0 0 19px;width:19px;height:19px}
.products{position:absolute;left:33px;top:420px}
.products-title{font-weight:800;font-size:21px;letter-spacing:.3px;margin-bottom:6px}
.product-lists{display:flex;gap:6px}
.product-list{list-style:none}
.product-list li{position:relative;padding-left:13px;font-weight:500;font-size:13px;line-height:1.05;margin-bottom:5px;text-transform:uppercase;letter-spacing:.6px}
.product-list li::before{content:"";position:absolute;left:1px;top:4px;width:6px;height:6px;border-radius:50%;background:var(--white)}
.photo-circle{position:absolute;border:4px solid var(--white);border-radius:50%}
.circle-team{left:435px;top:406px;width:122px;height:122px;background:radial-gradient(circle at 45% 40%,#b9b2aa,#5d5a5c 70%,#383840)}
.circle-advisor{left:535px;top:402px;width:84px;height:84px;background:radial-gradient(circle at 55% 45%,#e9e3dd,#a8876e 70%,#6e5040)}
.circle-interior{left:522px;top:472px;width:86px;height:86px;background:radial-gradient(circle at 50% 45%,#f2e2c6,#d1a676 60%,#9a6a44)}
.contact{
  position:absolute;left:0;top:548px;width:640px;height:92px;
  background:linear-gradient(90deg,var(--navy) 0%,var(--royal) 100%);
}
.phone-icon{position:absolute;left:25px;top:12px;width:66px;height:66px}
.call{position:absolute;left:99px;top:12px;font-family:"Bebas Neue",sans-serif;font-size:36px;line-height:.95;letter-spacing:-.2px}
.call-number{color:var(--gold)}
.address{position:absolute;left:422px;top:14px;font-style:normal;font-size:11px;line-height:1.12;font-weight:500}
.address .pin{position:absolute;left:-15px;top:1px;width:11px;height:14px}
.nmls{display:inline-block;margin-top:4px;background:var(--white);color:var(--navy);font-weight:800;font-size:11.5px;padding:1px 4px}
</style>
</head>
<body>
<main class="ad">
  <div class="hero-photo" role="img" aria-label="Photo of a businessman in shirt and tie reviewing a tablet at a desk by office windows"></div>

  <div class="brand">
    <div class="brand-mark"></div>
    <div class="brand-name">Brightmoor Lending Partners</div>
  </div>

  <h1 class="headline">
    <span class="headline-main">Commercial</span>
    <span class="headline-sub">Loan Originators</span>
  </h1>

  <div class="rule" style="top:320px"></div>
  <section class="benefits">
    <ul class="benefit-col">
      <li class="benefit"><svg class="tick" viewBox="0 0 20 20"><circle cx="10" cy="10" r="10" fill="#fff"/><path d="M5.5 10.5l3 3 6-6.5" fill="none" stroke="#2a4fb5" stroke-width="2.6" stroke-linecap="round" stroke-linejoin="round"/></svg>No licensing required</li>
      <li class="benefit"><svg class="tick" viewBox="0 0 20 20"><circle cx="10" cy="10" r="10" fill="#fff"/><path d="M5.5 10.5l3 3 6-6.5" fill="none" stroke="#2a4fb5" stroke-width="2.6" stroke-linecap="round" stroke-linejoin="round"/></svg>Lend nationwide with<br>few exceptions</li>
    </ul>
    <ul class="benefit-col">
      <li class="benefit"><svg class="tick" viewBox="0 0 20 20"><circle cx="10" cy="10" r="10" fill="#fff"/><path d="M5.5 10.5l3 3 6-6.5" fill="none" stroke="#2a4fb5" stroke-width="2.6" stroke-linecap="round" stroke-linejoin="round"/></svg>Competitive compensation</li>
      <li class="benefit"><svg class="tick" viewBox="0 0 20 20"><circle cx="10" cy="10" r="10" fill="#fff"/><path d="M5.5 10.5l3 3 6-6.5" fill="none" stroke="#2a4fb5" stroke-width="2.6" stroke-linecap="round" stroke-linejoin="round"/></svg>You find the investors and<br>we handle the rest!!!</li>
    </ul>
  </section>
  <div class="rule" style="top:408px"></div>

  <section class="products">
    <h2 class="products-title">PRODUCTS</h2>
    <div class="product-lists">
      <ul class="product-list">
        <li>Debt service coverage<br>loans (DSCR)</li>
        <li>Fix &amp; flip financing</li>
        <li>Ground up construction</li>
      </ul>
      <ul class="product-list">
        <li>Bridge loans</li>
        <li>Portfolio loans</li>
        <li>And many more.....</li>
      </ul>
    </div>
  </section>

  <div class="rule" style="top:542px"></div>
  <footer class="contact">
    <svg class="phone-icon" viewBox="0 0 66 66">
      <circle cx="33" cy="33" r="31" fill="none" stroke="#fff" stroke-width="2.5"/>
      <path d="M22 20c2-2 4-2 5 0l3 5c1 2 0 3-1 4l-2 2c1 4 5 8 9 9l2-2c1-1 2-2 4-1l5 3c2 1 2 3 0 5l-3 3c-10 1-25-14-24-24z" fill="#fff"/>
      <path d="M35 19a12 12 0 0 1 12 12M35 24a7 7 0 0 1 7 7" fill="none" stroke="#fff" stroke-width="2.5" stroke-linecap="round"/>
    </svg>
    <p class="call">CALL <span class="call-number">(800) 417-9265</span> X24<br>FOR MORE INFORMATION</p>
    <address class="address">
      <svg class="pin" viewBox="0 0 12 16"><path d="M6 0a6 6 0 0 0-6 6c0 4 6 10 6 10s6-6 6-10a6 6 0 0 0-6-6z" fill="#fff"/><circle cx="6" cy="6" r="2.3" fill="#263f9a"/></svg>
      Brightmoor Lending Partners, Inc.<br>
      7200 Warbleton Avenue,<br>
      Harrow Springs, MD 21987<br>
      <span class="nmls">NMLS #318640</span>
    </address>
  </footer>

  <div class="photo-circle circle-team" role="img" aria-label="Photo of advisors meeting with clients at a table"></div>
  <div class="photo-circle circle-advisor" role="img" aria-label="Photo of a smiling businesswoman"></div>
  <div class="photo-circle circle-interior" role="img" aria-label="Photo of a bright renovated home kitchen"></div>
</main>
</body>
</html>
```